Wheelchair Accessible Accommodation

We are 100% online, promoting accommodation details and booking facilities for wheelchair dependant travellers.
Listings will only be accommodation providers which meet our specific criteria.

Target Market(s)

Wheelchair dependant people and their companions

Industry/Entity Type

Accommodation

Contact Information for Business Card

Name, mobile phone number, email address, website address

```html
<!DOCTYPE html>
<html lang="en">
<head>
<meta charset="utf-8">
<title>Rollway Stays – Business Card</title>
<link href="https://fonts.googleapis.com/css2?family=Open+Sans:wght@400;600;800&display=swap" rel="stylesheet">
<style>
  :root {
    --stage: #7b8594;
    --card-dark: #2f2e30;
    --card-dark-edge: #3a393b;
    --card-light: #f6f6f6;
    --brand-red: #e3173a;
    --ink: #2b2b2b;
    --ink-soft: #555555;
    --on-dark: #e8e8e8;
  }
  * { box-sizing: border-box; margin: 0; padding: 0; }
  html, body {
    width: 1200px; height: 1024px; overflow: hidden;
    background: var(--stage);
    font-family: "Open Sans", Arial, sans-serif;
  }
  .canvas { position: relative; width: 1200px; height: 1024px; }

  .card {
    position: absolute;
    width: 630px; height: 360px;
    border-radius: 22px;
  }

  /* Back side */
  .card--back {
    left: 70px; top: 90px;
    background: radial-gradient(ellipse at 50% 40%, var(--card-dark-edge), var(--card-dark));
  }
  .card--back .brand {
    position: absolute; left: 0; right: 0; top: 130px;
    display: flex; align-items: center; justify-content: center; gap: 14px;
  }
  .brand__dot {
    width: 20px; height: 20px; border-radius: 50%;
    background: var(--brand-red);
  }
  .card--back .brand__name {
    font-weight: 800; font-size: 46px; letter-spacing: -0.5px;
    color: var(--on-dark);
  }
  .card--back .web {
    position: absolute; left: 0; right: 0; bottom: 60px;
    text-align: center; font-size: 17px; color: var(--on-dark);
    letter-spacing: 0.3px;
  }

  /* Front side */
  .card--front {
    left: 500px; top: 570px;
    background: linear-gradient(135deg, #ffffff, var(--card-light) 60%, #e9e9e9);
  }
  .card--front .brand {
    position: absolute; left: 48px; top: 52px;
    display: flex; align-items: center; gap: 12px;
  }
  .card--front .brand__name {
    font-weight: 800; font-size: 38px; letter-spacing: -0.5px;
    color: var(--brand-red);
  }
  .divider {
    position: absolute; left: 48px; top: 150px;
  }
  .holder {
    position: absolute; right: 48px; top: 188px;
    font-weight: 800; font-size: 24px; color: var(--ink);
  }
  .contacts {
    position: absolute; right: 48px; top: 232px;
    list-style: none; text-align: right;
  }
  .contacts li {
    display: flex; align-items: center; justify-content: flex-end; gap: 8px;
    font-size: 17px; color: var(--ink-soft); line-height: 30px;
  }
  .contacts svg { width: 12px; height: 12px; fill: var(--brand-red); }
</style>
</head>
<body>
<main class="canvas">

  <section class="card card--back" aria-label="Card back">
    <div class="brand">
      <span class="brand__dot"></span>
      <span class="brand__name">Rollway Stays</span>
    </div>
    <p class="web">www.rollwaystays.example</p>
  </section>

  <section class="card card--front" aria-label="Card front">
    <div class="brand">
      <span class="brand__dot"></span>
      <span class="brand__name">Rollway Stays</span>
    </div>

    <svg class="divider" width="260" height="40" viewBox="0 0 260 40" aria-hidden="true">
      <path d="M0 38 L260 0 L260 2 L0 40 Z" fill="var(--brand-red)"/>
    </svg>

    <h1 class="holder">Alex Moreno</h1>
    <ul class="contacts">
      <li>
        <svg viewBox="0 0 12 12" aria-hidden="true"><rect x="3" y="0" width="6" height="12" rx="1.2"/><rect x="4.2" y="1.5" width="3.6" height="7" fill="#fff"/></svg>
        555-014-2290
      </li>
      <li>
        <svg viewBox="0 0 12 12" aria-hidden="true"><rect x="0" y="2" width="12" height="8"/><path d="M0 2 L6 7 L12 2" stroke="#fff" stroke-width="1.2" fill="none"/></svg>
        hello@rollwaystays.example
      </li>
      <li>
        <svg viewBox="0 0 12 12" aria-hidden="true"><circle cx="6" cy="6" r="6"/><path d="M0 6 H12 M6 0 V12" stroke="#fff" stroke-width="1"/></svg>
        www.rollwaystays.example
      </li>
    </ul>
  </section>

</main>
</body>
</html>
```